Energy trading company (Voltrisa) needs a business card

We need a business card for a company based in Central America. Our main purpose is trading energy . We already have the logo but we need some good creativity to design a high impact business card. Colors blue, orange, green can be used or we would like to see good combinatios with our logo

Target Market(s)

Energy

Industry/Entity Type

Power Generation

Contact Information for Business Card

Logo , headquarters , name, background

Font styles to use
Serif
Sans Serif

Colors

Designer to choose colors to be used in the design.

Requirements
Must have
• it must have a fresh and clean view
Nice to have
• good backgrounds that combine with the logo
Should not have
• too much words

```html
<!DOCTYPE html>
<html lang="en">
<head>
<meta charset="utf-8">
<title>Voltrisa — Business Card</title>
<link rel="stylesheet" href="https://fonts.googleapis.com/css2?family=Bebas+Neue&family=Montserrat:wght@500;600&display=swap">
<style>
  :root {
    --orange: #f39321;
    --navy: #1b5aa6;
    --sky: #7dd3f5;
    --mid-blue: #4f98d3;
    --white: #ffffff;
  }
  html, body {
    margin: 0;
    padding: 0;
    width: 1200px;
    height: 720px;
    overflow: hidden;
    background: var(--white);
  }
  .card {
    position: relative;
    width: 1125px;
    height: 675px;
    transform: scale(1.066667);
    transform-origin: 0 0;
    overflow: hidden;
    font-family: "Montserrat", sans-serif;
  }
  .card-background {
    position: absolute;
    inset: 0;
    width: 1125px;
    height: 675px;
  }
  .brand {
    position: absolute;
    left: 110px;
    top: 118px;
    width: 410px;
    display: flex;
    flex-direction: column;
    align-items: center;
    gap: 22px;
  }
  .brand-dot {
    width: 100px;
    height: 100px;
    border-radius: 50%;
    background: var(--orange);
  }
  .brand-name {
    margin: 0;
    font-weight: 500;
    font-size: 74px;
    line-height: 1;
    color: var(--orange);
    text-transform: uppercase;
    letter-spacing: 1px;
    white-space: nowrap;
  }
  .holder {
    position: absolute;
    left: 558px;
    top: 120px;
    width: 442px;
    height: 133px;
    background: var(--white);
    box-sizing: border-box;
    padding: 26px 0 0 24px;
  }
  .holder-name {
    margin: 0;
    font-weight: 600;
    font-size: 34px;
    line-height: 1.1;
    color: var(--orange);
    white-space: nowrap;
  }
  .holder-title {
    margin: 10px 0 0;
    font-weight: 600;
    font-size: 26px;
    line-height: 1.1;
    color: var(--navy);
    white-space: nowrap;
  }
  .location-bar {
    position: absolute;
    left: 152px;
    top: 367px;
    width: 818px;
    height: 173px;
    border-radius: 32px;
    background: linear-gradient(90deg, var(--sky) 0%, var(--mid-blue) 40%, var(--navy) 100%);
  }
  .location-arrow {
    position: absolute;
    left: 0;
    top: 62px;
    width: 72px;
    height: 50px;
  }
  .location-label {
    position: absolute;
    left: 104px;
    top: 32px;
    margin: 0;
    font-family: "Bebas Neue", "Oswald", sans-serif;
    font-weight: 400;
    font-size: 134px;
    line-height: 1;
    color: var(--white);
    letter-spacing: 1px;
    white-space: nowrap;
  }
  .location-dot {
    position: absolute;
    left: 762px;
    top: 38px;
    width: 98px;
    height: 98px;
    border-radius: 50%;
    background: var(--white);
  }
</style>
</head>
<body>
  <main class="card">
    <svg class="card-background" viewBox="0 0 1125 675" aria-hidden="true">
      <defs>
        <linearGradient id="ring-blue" x1="0" y1="0" x2="0" y2="675" gradientUnits="userSpaceOnUse">
          <stop offset="0" stop-color="#7dd3f5"/>
          <stop offset="0.45" stop-color="#3f86c8"/>
          <stop offset="1" stop-color="#1b5aa6"/>
        </linearGradient>
        <linearGradient id="glow-peach" x1="470" y1="0" x2="690" y2="0" gradientUnits="userSpaceOnUse">
          <stop offset="0" stop-color="#ffffff"/>
          <stop offset="1" stop-color="#fbd3ad"/>
        </linearGradient>
        <linearGradient id="band-orange" x1="0" y1="0" x2="0" y2="675" gradientUnits="userSpaceOnUse">
          <stop offset="0" stop-color="#f08a1c"/>
          <stop offset="0.55" stop-color="#f6a21f"/>
          <stop offset="1" stop-color="#ffd21a"/>
        </linearGradient>
        <linearGradient id="field-green" x1="0" y1="0" x2="0" y2="675" gradientUnits="userSpaceOnUse">
          <stop offset="0" stop-color="#1fae4b"/>
          <stop offset="0.5" stop-color="#3cb54a"/>
          <stop offset="1" stop-color="#a5d06b"/>
        </linearGradient>
        <clipPath id="inner-disc">
          <circle cx="362" cy="330" r="336"/>
        </clipPath>
      </defs>

      <rect class="ring-field" width="1125" height="675" fill="url(#ring-blue)"/>
      <circle class="ring-line" cx="362" cy="345" r="398" fill="none" stroke="#ffffff" stroke-width="10"/>
      <circle class="ring-line" cx="362" cy="338" r="360" fill="none" stroke="#ffffff" stroke-width="8"/>
      <circle class="inner-disc" cx="362" cy="330" r="336" fill="#ffffff"/>
      <rect class="inner-glow" x="470" y="0" width="240" height="675" fill="url(#glow-peach)" clip-path="url(#inner-disc)"/>

      <circle class="band-blue" cx="-794" cy="0" r="1524" fill="none" stroke="url(#ring-blue)" stroke-width="80"/>
      <circle class="band-gap" cx="-794" cy="0" r="1568" fill="none" stroke="#ffffff" stroke-width="8"/>
      <circle class="band-orange" cx="-794" cy="0" r="1599" fill="none" stroke="url(#band-orange)" stroke-width="54"/>
      <circle class="band-gap" cx="-794" cy="0" r="1631" fill="none" stroke="#ffffff" stroke-width="10"/>
      <circle class="band-outer-blue" cx="-794" cy="0" r="1670" fill="none" stroke="url(#ring-blue)" stroke-width="70"/>
      <circle class="band-gap" cx="-794" cy="0" r="1710" fill="none" stroke="#ffffff" stroke-width="10"/>
      <circle class="band-green" cx="-794" cy="0" r="2215" fill="none" stroke="url(#field-green)" stroke-width="1000"/>

      <rect class="green-divider" x="1000" y="172" width="125" height="28" fill="#ffffff"/>
    </svg>

    <header class="brand">
      <span class="brand-dot" aria-hidden="true"></span>
      <h1 class="brand-name">Voltrisa</h1>
    </header>

    <section class="holder">
      <p class="holder-name">NAME : XXXXXXXX</p>
      <p class="holder-title">TITLE : XXXXXX</p>
    </section>

    <section class="location-bar">
      <svg class="location-arrow" viewBox="0 0 72 50" aria-hidden="true">
        <path d="M0 20 H44 V6 L70 25 L44 44 V30 H0 Z" fill="#ffffff"/>
      </svg>
      <h2 class="location-label">HEADQUARTERS</h2>
      <span class="location-dot" aria-hidden="true"></span>
    </section>
  </main>
</body>
</html>
```